App für weniger Konsum
Zielgruppe
Wir sind ein Startup, das Nutzer:innen in einem bewussteren Kaufverhalten stärkt. Dabei werden Nutzer:innen psychologischen Kaufprofilen zugeordnet und individuell auf dem Weg begleitet, weniger einzukaufen. Das stärkt die Finanzen und schützt die Umwelt.
Aufgabenstellung
Das Design sollte einerseits minimalismusorientierte Nutzer:innen ansprechen (clean, ruhig), aber auch Nutzer:innen ansprechen, die sich noch nicht mit weniger / besserem Konsum beschäftigt haben.
Es wäre toll folgende Slides zu haben:
- Anmeldung / Registrierung
- Quiz (Es soll direkt zu Beginn ein Quiz aus mehreren Slides geben, das Nutzer:innen einem Kauftypen zuordnet(
- Quizergebnis (Du bist Kauftyp XYZ...)
- Home-Screen der App / Navigation
- Statistiken: Du hast diesen Monat so viel gespart...
- Slide mit Einstellungen
- 'Challenge' Slide: 10 tage aussortieren

```html
<!DOCTYPE html>
<html lang="de">
<head>
<meta charset="utf-8">
<title>Bewusst Konsumieren – App Screens</title>
<link href="https://fonts.googleapis.com/css2?family=Inter:wght@400;500;600;700&display=swap" rel="stylesheet">
<style>
:root{
  --bg:#f3f3f3;
  --card:#ffffff;
  --ink:#141414;
  --muted:#8a8a8a;
  --soft:#f6f6f6;
  --line:#ececec;
  --lime:#c2f060;
  --lime-soft:#eefbd6;
  --green:#5aa300;
  --lilac:#eef0fc;
  --lilac-ink:#5560c8;
  --orange:#f08a3c;
  --red:#e0352b;
}
*{box-sizing:border-box;margin:0;padding:0}
html,body{width:1200px;height:3865px;overflow:hidden}
body{background:var(--bg);font-family:"Inter",sans-serif;color:var(--ink);position:relative}
.label{position:absolute;width:345px;text-align:center;font-size:10px;letter-spacing:1.2px;color:#a5a5a5;text-transform:uppercase}
.phone{position:absolute;width:345px;background:var(--card);border-radius:32px;box-shadow:0 8px 24px rgba(0,0,0,.08),0 0 0 1px rgba(0,0,0,.04);overflow:hidden}
.abs{position:absolute}
.center{left:0;right:0;text-align:center}
.btn{position:absolute;display:flex;align-items:center;justify-content:center;border-radius:30px;font-size:13px;font-weight:500}
.btn-outline{border:1px solid #e2e2e2;background:#fff}
.btn-lime{background:var(--lime)}
.btn-dark{background:var(--ink);color:#fff}
.round{position:absolute;border-radius:50%;display:flex;align-items:center;justify-content:center}
.eyebrow{font-size:10px;letter-spacing:1.2px;font-weight:600;color:var(--green);text-transform:uppercase}
.muted{color:var(--muted)}
.option{position:absolute;left:35px;width:278px;border:1px solid #e6e6e6;border-radius:18px;padding:20px 20px;box-shadow:0 2px 6px rgba(0,0,0,.03)}
.option h4{font-size:15px;font-weight:500;margin-bottom:9px}
.option p{font-size:11px;color:var(--muted);line-height:1.5}
.option svg{position:absolute;right:20px;top:22px}
.progress{position:absolute;left:22px;right:22px;top:4px;height:5px;border-radius:3px;background:#f0f0f0}
.progress i{display:block;height:100%;border-radius:3px;background:var(--lime)}
.next{width:45px;height:45px;background:var(--lime);box-shadow:0 4px 10px rgba(160,220,60,.4)}
.panel{position:absolute;left:35px;width:278px;background:var(--soft);border-radius:18px;padding:22px 20px}
.panel h4{font-size:15px;font-weight:600;margin:14px 0 10px}
.panel p{font-size:11px;color:var(--muted);line-height:1.6}
.tabbar{position:absolute;left:0;right:0;height:60px;border-top:1px solid var(--line);display:flex;justify-content:space-around;padding:0 20px;background:#fff;z-index:2}
.tab{display:flex;flex-direction:column;align-items:center;gap:6px;padding-top:16px;font-size:9px;color:#a5a5a5;width:60px}
.tab.on{color:var(--green);font-weight:600}
.group{position:absolute;left:33px;width:280px;border:1px solid #e8e8e8;border-radius:12px;overflow:hidden}
.row{height:47px;display:flex;align-items:center;justify-content:space-between;padding:0 14px;font-size:13px;font-weight:500;border-bottom:1px solid #eee}
.row:last-child{border-bottom:none}
.row span.val{font-size:12px;color:var(--muted);font-weight:400}
.sect{position:absolute;left:37px;font-size:10px;letter-spacing:1.3px;color:#9a9a9a;text-transform:uppercase}
</style>
</head>
<body>

<div class="label" style="left:40px;top:40px">1. Login &amp; Registrierung</div>
<div class="label" style="left:427px;top:40px">2. Quiz Intro</div>
<div class="label" style="left:813px;top:40px">3. Quiz Question 1</div>

<!-- 1 Login -->
<section class="phone" style="left:40px;top:67px;height:703px">
  <div class="abs" style="left:150px;top:80px;width:45px;height:45px;border-radius:12px;background:var(--soft)"></div>
  <h1 class="abs center" style="top:152px;font-size:25px;font-weight:500">Willkommen zurück</h1>
  <p class="abs center muted" style="top:194px;font-size:13px">Dein Begleiter für bewusstes Konsumieren.</p>
  <div class="btn btn-outline" style="left:33px;top:247px;width:279px;height:42px">Mit Obsta anmelden</div>
  <div class="btn btn-outline" style="left:33px;top:303px;width:279px;height:42px">Mit Suchro anmelden</div>
  <div class="abs" style="left:33px;top:395px;width:279px;display:flex;align-items:center;gap:14px;font-size:9px;letter-spacing:1.3px;color:#aaa">
    <i style="flex:1;height:1px;background:#e8e8e8"></i>ODER MIT EMAIL<i style="flex:1;height:1px;background:#e8e8e8"></i></div>
  <p class="abs" style="left:47px;top:442px;font-size:10px;color:#555">Email Adresse</p>
  <div class="abs" style="left:33px;top:462px;width:279px;height:45px;background:var(--soft);border-radius:12px"></div>
  <div class="btn btn-lime" style="left:33px;top:530px;width:279px;height:45px;font-weight:600">Weiter</div>
  <p class="abs center" style="top:656px;font-size:9px;color:#aaa">Mit der Anmeldung akzeptierst du unsere <u>AGB</u>.</p>
</section>

<!-- 2 Quiz intro -->
<section class="phone" style="left:427px;top:67px;height:703px">
  <div class="round" style="left:33px;top:47px;width:33px;height:33px;border:1px solid #e4e4e4">
    <svg width="12" height="12" viewBox="0 0 12 12" stroke="#666" stroke-width="1.4"><path d="M2 2l8 8M10 2l-8 8"/></svg>
  </div>
  <div class="round" style="left:120px;top:145px;width:105px;height:105px;background:linear-gradient(135deg,#eaf7d8,#e6ecf3)">
    <svg width="40" height="40" viewBox="0 0 24 24" fill="none" stroke="#4f9e10" stroke-width="1.6" stroke-linejoin="round"><path d="M10 4l1.6 4.4L16 10l-4.4 1.6L10 16l-1.6-4.4L4 10l4.4-1.6z"/><path d="M18 3v4M16 5h4M17 15v3M15.5 16.5h3"/></svg>
  </div>
  <h1 class="abs center" style="top:285px;font-size:25px;font-weight:500;line-height:1.2">Lerne deinen<br>Kaufstil kennen</h1>
  <p class="abs center muted" style="top:358px;left:55px;right:55px;font-size:14px;line-height:1.7">Dieses kurze Quiz hilft uns zu verstehen, was deine Kaufentscheidungen antreibt.</p>
  <div class="abs" style="left:47px;top:463px;width:252px;height:85px;background:var(--soft);border-radius:12px;padding:20px 22px;font-size:11px;color:#666;line-height:2.4">
    <div style="display:flex;align-items:center;gap:8px"><svg width="12" height="12" viewBox="0 0 12 12" fill="none" stroke="#5aa300" stroke-width="1.2"><circle cx="6" cy="6" r="5"/><path d="M6 3v3l2 1"/></svg>Dauer: ca. 2 Minuten</div>
    <div style="display:flex;align-items:center;gap:8px"><svg width="12" height="12" viewBox="0 0 12 12" fill="none" stroke="#5aa300" stroke-width="1.2"><circle cx="6" cy="6" r="5"/><path d="M3.5 6l2 2 3-3.5"/></svg>Daten bleiben privat</div>
  </div>
  <div class="btn btn-dark" style="left:33px;top:615px;width:279px;height:53px;justify-content:space-between;padding:0 26px">Starten
    <svg width="14" height="14" viewBox="0 0 14 14" fill="none" stroke="#fff" stroke-width="1.5"><path d="M2 7h10M8 3l4 4-4 4"/></svg></div>
</section>

<!-- 3 Question 1 -->
<section class="phone" style="left:813px;top:67px;height:703px">
  <div class="progress"><i style="width:50px"></i></div>
  <p class="abs eyebrow" style="left:35px;top:60px">Situation 01/05</p>
  <h2 class="abs" style="left:35px;top:82px;width:285px;font-size:19.5px;font-weight:400;line-height:1.4;letter-spacing:-.2px">Du betrittst ein Geschäft.<br>Wohin geht dein erster Blick?</h2>
  <div class="option" style="top:245px;height:87px"><h4>Zur Sale-Abteilung</h4><p>Ich liebe es, Schnäppchen zu finden.</p>
    <svg width="14" height="14" viewBox="0 0 14 14" fill="none" stroke="#aaa" stroke-width="1.2"><path d="M3 11L11 3"/><circle cx="4" cy="4" r="1.3"/><circle cx="10" cy="10" r="1.3"/></svg></div>
  <div class="option" style="top:347px;height:87px"><h4>Zu den Neuheiten</h4><p>Ich möchte wissen, was im Trend liegt.</p>
    <svg width="14" height="14" viewBox="0 0 24 24" fill="none" stroke="#aaa" stroke-width="1.6"><path d="M10 4l1.6 4.4L16 10l-4.4 1.6L10 16l-1.6-4.4L4 10l4.4-1.6z"/><path d="M18 3v4M16 5h4"/></svg></div>
  <div class="option" style="top:447px;height:87px"><h4>Gezielt zum Produkt</h4><p>Ich hole nur, was ich brauche.</p>
    <svg width="14" height="14" viewBox="0 0 14 14" fill="none" stroke="#aaa" stroke-width="1.2"><circle cx="7" cy="7" r="5.5"/><circle cx="7" cy="7" r="3"/><circle cx="7" cy="7" r=".8"/></svg></div>
  <div class="round next" style="left:267px;top:622px"><svg width="16" height="16" viewBox="0 0 14 14" fill="none" stroke="#111" stroke-width="1.5"><path d="M2 7h10M8 3l4 4-4 4"/></svg></div>
</section>

<div class="label" style="left:40px;top:811px">4. Quiz Question 2</div>
<div class="label" style="left:427px;top:811px">8. Quiz Result</div>
<div class="label" style="left:813px;top:811px">9. Profile Detail</div>

<!-- 4 Question 2 -->
<section class="phone" style="left:40px;top:837px;height:703px">
  <div class="progress"><i style="width:118px"></i></div>
  <p class="abs eyebrow" style="left:33px;top:60px">Situation 02/05</p>
  <h2 class="abs" style="left:33px;top:82px;width:290px;font-size:19.5px;font-weight:400;line-height:1.4;letter-spacing:-.2px">Ein stressiger Tag geht zu<br>Ende. Du siehst eine Werbung.<br>Was fühlst du?</h2>
  <div class="option" style="left:33px;top:234px;height:102px"><h4>Belohnung</h4><p>Der Kauf würde mir sofort gute Laune machen.</p>
    <svg width="14" height="14" viewBox="0 0 14 14" fill="none" stroke="#aaa" stroke-width="1.1"><rect x="2" y="5" width="10" height="7"/><path d="M1.5 5h11M7 5v7M7 5C5 2 3 3 4.5 5M7 5c2-3 4-2 2.5 0"/></svg></div>
  <div class="option" style="left:33px;top:353px;height:102px"><h4>Gleichgültigkeit</h4><p>Ich scrolle weiter, es berührt mich heute nicht.</p>
    <svg width="14" height="14" viewBox="0 0 14 14" fill="none" stroke="#aaa" stroke-width="1.1"><circle cx="7" cy="7" r="5.5"/><path d="M4.8 8.8h4.4"/><circle cx="5" cy="5.8" r=".5"/><circle cx="9" cy="5.8" r=".5"/></svg></div>
  <div class="option" style="left:33px;top:471px;height:102px"><h4>Kaufdruck</h4><p>Ich habe Angst, ein gutes Angebot zu verpassen.</p>
    <svg width="14" height="14" viewBox="0 0 14 14" fill="none" stroke="#aaa" stroke-width="1.1"><circle cx="7" cy="7" r="5.5"/><path d="M7 4v3.5M7 9.5v.3"/></svg></div>
  <div class="round next" style="left:267px;top:622px"><svg width="16" height="16" viewBox="0 0 14 14" fill="none" stroke="#111" stroke-width="1.5"><path d="M2 7h10M8 3l4 4-4 4"/></svg></div>
</section>

<!-- 8 Result -->
<section class="phone" style="left:427px;top:837px;height:703px">
  <div class="abs" style="left:8px;right:8px;top:0;bottom:8px;border-radius:0 0 26px 26px;background:linear-gradient(180deg,#fff 45%,#eef9d8 100%)"></div>
  <div class="round" style="left:108px;top:138px;width:130px;height:130px;background:#fff;border:2px solid #eef5e2;box-shadow:0 6px 18px rgba(0,0,0,.05)">
    <svg width="50" height="50" viewBox="0 0 24 24" fill="none" stroke="#5aa300" stroke-width="2.2" stroke-linejoin="round" stroke-linecap="round"><path d="M12 20s-8-5-8-11a4.5 4.5 0 0 1 8-2.5A4.5 4.5 0 0 1 20 9c0 6-8 11-8 11z"/><path d="M8 12l3-2 3 3 2-2"/></svg>
  </div>
  <p class="abs center eyebrow" style="top:305px">Dein Ergebnis</p>
  <h1 class="abs center" style="top:330px;font-size:29px;font-weight:500;line-height:1.15">Der emotionale<br>Ausgleicher</h1>
  <p class="abs center muted" style="top:412px;left:30px;right:30px;font-size:14px;line-height:1.75">Du nutzt Einkäufe oft unbewusst, um<br>für Balance in stressigen Zeiten zu<br>sorgen.</p>
  <div class="btn btn-dark" style="left:90px;top:519px;width:165px;height:45px;gap:8px">Mehr erfahren
    <svg width="10" height="10" viewBox="0 0 10 10" fill="none" stroke="#fff" stroke-width="1.3"><path d="M2 4l3 3 3-3"/></svg></div>
</section>

<!-- 9 Profile detail -->
<section class="phone" style="left:813px;top:837px;height:703px">
  <div class="round" style="left:35px;top:48px;width:30px;height:30px;background:var(--soft)"><svg width="13" height="13" viewBox="0 0 14 14" fill="none" stroke="#222" stroke-width="1.5"><path d="M12 7H2M6 3L2 7l4 4"/></svg></div>
  <p class="abs" style="left:80px;top:55px;font-size:15px;font-weight:500">Dein Profil</p>
  <h1 class="abs" style="left:35px;top:105px;font-size:25px;font-weight:500;line-height:1.2">Der emotionale<br>Ausgleicher</h1>
  <div class="panel" style="top:192px;height:174px">
    <div class="round" style="position:static;width:32px;height:32px;background:#e6e8fb"><svg width="15" height="15" viewBox="0 0 24 24" fill="none" stroke="#5a64d6" stroke-width="2" stroke-linejoin="round"><path d="M13 2L4 14h7l-1 8 9-12h-7z"/></svg></div>
    <h4>Der Auslöser</h4><p>Oft ist es nicht das Produkt selbst, sondern das Gefühl des "Sich-Gönnens" nach Anstrengung oder Stress.</p>
  </div>
  <div class="panel" style="top:387px;height:174px">
    <div class="round" style="position:static;width:32px;height:32px;background:#fde9d9"><svg width="15" height="15" viewBox="0 0 24 24" fill="none" stroke="#e8782c" stroke-width="2" stroke-linejoin="round"><path d="M12 3l10 18H2z"/><path d="M12 10v5M12 18v.2"/></svg></div>
    <h4>Die Falle</h4><p>Kurzfristige Freude verwandelt sich schnell in Gleichgültigkeit gegenüber dem Gegenstand.</p>
  </div>
  <div class="abs" style="left:35px;top:580px;width:278px;height:30px;border-radius:18px 18px 0 0;background:linear-gradient(180deg,#f3fbe3,#fff)"></div>
  <div class="btn btn-dark" style="left:35px;top:615px;width:278px;height:47px">Mein Dashboard öffnen</div>
</section>

<div class="label" style="left:40px;top:1580px">10. Home Dashboard</div>
<div class="label" style="left:427px;top:1580px">11. Statistics</div>
<div class="label" style="left:813px;top:1580px">12. Challenge Details</div>

<!-- 10 Home -->
<section class="phone" style="left:40px;top:1606px;height:726px">
  <p class="abs" style="left:33px;top:50px;font-size:11px;color:#555">Dienstag, 24. Okt</p>
  <h2 class="abs" style="left:33px;top:70px;font-size:20px;font-weight:500">Guten Morgen, Anna</h2>
  <div class="round" role="img" aria-label="Profilbild der Nutzerin" style="left:280px;top:58px;width:33px;height:33px;background:linear-gradient(180deg,#e9eee8,#cfd8cc)"></div>
  <div class="abs" style="left:33px;top:120px;width:279px;height:203px;background:var(--lilac);border-radius:22px;padding:20px 20px">
    <span style="display:inline-block;background:#dde1fa;color:var(--lilac-ink);font-size:8px;font-weight:600;letter-spacing:1px;padding:3px 7px;border-radius:6px">DAILY INSIGHT</span>
    <p style="font-size:16.5px;line-height:1.5;margin:12px 0 10px;letter-spacing:-.2px">"Nicht zu kaufen ist auch eine Einnahme."</p>
    <p style="font-size:11px;line-height:1.5;color:#8a90c6">Überlege heute bei einer Ausgabe: Wie lange müsstest du dafür arbeiten?</p>
    <p style="font-size:11px;color:var(--lilac-ink);font-weight:500;margin-top:20px">Gedanken notieren &nbsp;→</p>
  </div>
  <div class="abs" style="left:33px;top:351px;width:132px;height:133px;border:1px solid #e8e8e8;border-radius:18px;padding:18px 18px">
    <div class="round" style="position:static;width:30px;height:30px;background:var(--lime-soft)"><svg width="14" height="14" viewBox="0 0 24 24" fill="none" stroke="#5aa300" stroke-width="2"><path d="M5 12a7 6 0 0 1 12-3h2v4l-2 1v3h-3v-2H9v2H6v-3a6 6 0 0 1-1-2z"/></svg></div>
    <p style="font-size:20px;font-weight:600;margin-top:18px">42€</p>
    <p style="font-size:9px;color:var(--muted);line-height:1.3;margin-top:4px">Diese Woche<br>gespart</p>
  </div>
  <div class="abs" style="left:180px;top:351px;width:132px;height:133px;border:1px solid #e8e8e8;border-radius:18px;padding:18px 18px">
    <div class="round" style="position:static;width:30px;height:30px;background:#fdeadc"><svg width="14" height="14" viewBox="0 0 24 24" fill="none" stroke="#e8782c" stroke-width="2"><path d="M2 12h5l3-7 4 14 3-7h5"/></svg></div>
    <p style="font-size:20px;font-weight:600;margin-top:18px">3</p>
    <p style="font-size:9px;color:var(--muted);margin-top:4px">Impulse vermieden</p>
  </div>
  <p class="abs" style="left:33px;top:515px;font-size:14px;font-weight:500">Aktive Challenge</p>
  <div class="abs" style="left:33px;top:549px;width:279px;height:80px;border:1px solid #e8e8e8;border-radius:18px;padding:8px;display:flex;align-items:center;gap:14px">
    <div style="width:64px;height:64px;border-radius:14px;background:var(--soft);display:flex;align-items:center;justify-content:center;font-size:20px;font-weight:600">04</div>
    <div style="flex:1;padding-right:14px"><p style="font-size:13px;font-weight:500">Newsletter Detox</p>
      <div style="height:5px;background:#eee;border-radius:3px;margin:8px 0 6px"><i style="display:block;width:40%;height:100%;background:var(--lime);border-radius:3px"></i></div>
      <p style="font-size:9px;color:var(--muted)">Tag 4 von 10</p></div>
  </div>
  <nav class="tabbar" style="top:640px">
    <div class="tab on"><svg width="18" height="18" viewBox="0 0 24 24" fill="#5aa300"><path d="M3 10l9-7 9 7v11H3z"/></svg>Home</div>
    <div class="tab"><svg width="18" height="18" viewBox="0 0 24 24" fill="none" stroke="#aaa" stroke-width="1.8"><path d="M6 20v-6M12 20V4M18 20v-9"/></svg>Statistik</div>
    <div class="tab"><svg width="18" height="18" viewBox="0 0 24 24" fill="none" stroke="#aaa" stroke-width="1.6"><path d="M12 3l9 5-9 5-9-5z"/><path d="M3 12l9 5 9-5M3 16l9 5 9-5"/></svg>Challenge</div>
    <div class="tab"><svg width="18" height="18" viewBox="0 0 24 24" fill="#aaa"><circle cx="5" cy="12" r="1.6"/><circle cx="12" cy="12" r="1.6"/><circle cx="19" cy="12" r="1.6"/></svg>Menü</div>
  </nav>
</section>

<!-- 11 Statistics -->
<section class="phone" style="left:427px;top:1606px;height:703px">
  <h2 class="abs" style="left:33px;top:50px;font-size:20px;font-weight:500">Deine Erfolge</h2>
  <span class="abs" style="left:254px;top:52px;font-size:10px;color:#666;border:1px solid #e4e4e4;border-radius:12px;padding:3px 10px">Oktober</span>
  <p class="abs center" style="top:128px;font-size:11px;color:#555">Gespart durch Bewusstsein</p>
  <p class="abs center" style="top:145px;font-size:40px;font-weight:500">245€</p>
  <p class="abs center" style="top:198px;font-size:11px;color:var(--green)">↗ +120€ zum Vormonat</p>
  <div class="abs" style="left:43px;top:337px;width:57px;height:35px;background:#f2f2f2"></div>
  <div class="abs" style="left:111px;top:312px;width:57px;height:60px;background:#f2f2f2"></div>
  <div class="abs" style="left:178px;top:324px;width:54px;height:48px;background:#f2f2f2"></div>
  <div class="abs" style="left:240px;top:269px;width:66px;height:103px;background:#a6e63a"></div>
  <span class="abs" style="left:242px;top:242px;font-size:10px;color:#fff;background:#111;padding:3px 8px;border-radius:3px">Woche 4</span>
  <p class="abs" style="left:33px;top:406px;font-size:10px;letter-spacing:1.3px;color:#9a9a9a">HIGHLIGHTS</p>
  <div class="abs" style="left:33px;top:435px;width:279px;height:87px;background:var(--soft);border-radius:14px;padding:16px 14px 0 60px">
    <div class="round" style="left:14px;top:18px;width:30px;height:30px;background:#efe4fb"><svg width="14" height="14" viewBox="0 0 24 24" fill="none" stroke="#9b5de5" stroke-width="2"><circle cx="12" cy="12" r="9"/><path d="M12 4v16M9 8l3 4 3-4"/></svg></div>
    <p style="font-size:13px;font-weight:500;margin-bottom:6px">3x "Nein" gesagt</p>
    <p style="font-size:11px;color:var(--muted);line-height:1.45">Du hast drei Impulskäufe in der Kategorie "Technik" vermieden.</p>
  </div>
  <div class="abs" style="left:33px;top:534px;width:279px;height:87px;background:var(--soft);border-radius:14px;padding:16px 14px 0 60px">
    <div class="round" style="left:14px;top:18px;width:30px;height:30px;background:#e2ebfb"><svg width="14" height="14" viewBox="0 0 24 24" fill="none" stroke="#4a7fd8" stroke-width="2"><circle cx="12" cy="12" r="9"/><path d="M12 7v5l3 2"/></svg></div>
    <p style="font-size:13px;font-weight:500;margin-bottom:6px">24h Wartezeit eingehalten</p>
    <p style="font-size:11px;color:var(--muted);line-height:1.45">Bei deinem Wunschzettel hast du Geduld bewiesen.</p>
  </div>
  <nav class="tabbar" style="top:621px">
    <div class="tab"><svg width="18" height="18" viewBox="0 0 24 24" fill="none" stroke="#aaa" stroke-width="1.8"><path d="M3 10l9-7 9 7v11H3z"/><path d="M10 21v-6h4v6"/></svg>Home</div>
    <div class="tab on"><svg width="18" height="18" viewBox="0 0 24 24" fill="none" stroke="#5aa300" stroke-width="2.2"><path d="M6 20v-6M12 20V4M18 20v-9"/></svg>Statistik</div>
    <div class="tab"><svg width="18" height="18" viewBox="0 0 24 24" fill="none" stroke="#aaa" stroke-width="1.6"><path d="M12 3l9 5-9 5-9-5z"/><path d="M3 12l9 5 9-5M3 16l9 5 9-5"/></svg>Challenge</div>
    <div class="tab"><svg width="18" height="18" viewBox="0 0 24 24" fill="#aaa"><circle cx="5" cy="12" r="1.6"/><circle cx="12" cy="12" r="1.6"/><circle cx="19" cy="12" r="1.6"/></svg>Menü</div>
  </nav>
</section>

<!-- 12 Challenge -->
<section class="phone" style="left:813px;top:1606px;height:703px">
  <div class="round" style="left:35px;top:48px;width:30px;height:30px;background:var(--soft)"><svg width="13" height="13" viewBox="0 0 14 14" fill="none" stroke="#222" stroke-width="1.5"><path d="M12 7H2M6 3L2 7l4 4"/></svg></div>
  <div class="round" style="left:283px;top:48px;width:30px;height:30px"><svg width="15" height="15" viewBox="0 0 24 24" fill="none" stroke="#222" stroke-width="1.8"><circle cx="18" cy="5" r="2.5"/><circle cx="6" cy="12" r="2.5"/><circle cx="18" cy="19" r="2.5"/><path d="M8.2 10.8l7.6-4.6M8.2 13.2l7.6 4.6"/></svg></div>
  <div class="abs center" style="top:103px"><span style="font-size:9px;font-weight:600;letter-spacing:1px;color:var(--green);background:var(--lime-soft);padding:3px 9px;border-radius:10px">CHALLENGE</span></div>
  <h1 class="abs center" style="top:130px;font-size:26px;font-weight:500;line-height:1.15">10 Tage<br>Aussortieren</h1>
  <p class="abs center muted" style="top:200px;left:40px;right:40px;font-size:13px;line-height:1.5">Schaffe Raum für Neues, indem du Altes loslässt.</p>
  <div class="abs" style="left:35px;top:267px;width:278px;height:241px;border:1px solid #e6e6e6;border-radius:22px;box-shadow:0 6px 16px rgba(0,0,0,.05);text-align:center">
    <div class="round" style="left:119px;top:20px;width:40px;height:40px;background:var(--lime);font-size:14px;font-weight:600">01</div>
    <p style="margin-top:77px;font-size:16px;font-weight:600">Der Kleiderschrank</p>
    <p style="margin:10px 22px 0;font-size:11px;color:var(--muted);line-height:1.6">Finde 3 Teile, die du seit einem Jahr nicht getragen hast. Spende oder verkaufe sie heute.</p>
    <div class="btn btn-dark" style="left:20px;top:181px;width:238px;height:41px;border-radius:10px;font-size:11px;gap:7px">
      <svg width="12" height="12" viewBox="0 0 12 12" fill="none" stroke="#fff" stroke-width="1.2"><circle cx="6" cy="6" r="5"/><path d="M3.5 6l2 2 3-3.5"/></svg>Als erledigt markieren</div>
  </div>
  <div class="abs" style="left:44px;top:530px;font-size:12px;font-weight:500;line-height:33px">
    <div style="display:flex;align-items:center;gap:24px"><i style="width:9px;height:9px;border:1px solid #ccc;border-radius:50%"></i>Tag 02: Digitale Abos prüfen</div>
    <div style="display:flex;align-items:center;gap:24px"><i style="width:9px;height:9px;border:1px solid #ccc;border-radius:50%"></i>Tag 03: Vorratskammer leeren</div>
    <div style="display:flex;align-items:center;gap:24px"><i style="width:9px;height:9px;border:1px solid #ccc;border-radius:50%"></i>Tag 04: Badezimmer Check</div>
  </div>
  <nav class="tabbar" style="top:621px">
    <div class="tab"><svg width="18" height="18" viewBox="0 0 24 24" fill="none" stroke="#aaa" stroke-width="1.8"><path d="M3 10l9-7 9 7v11H3z"/><path d="M10 21v-6h4v6"/></svg>Home</div>
    <div class="tab"><svg width="18" height="18" viewBox="0 0 24 24" fill="none" stroke="#aaa" stroke-width="1.8"><path d="M6 20v-6M12 20V4M18 20v-9"/></svg>Statistik</div>
    <div class="tab on"><svg width="18" height="18" viewBox="0 0 24 24" fill="#5aa300" stroke="#5aa300" stroke-width="1.6" stroke-linejoin="round"><path d="M12 3l9 5-9 5-9-5z"/><path d="M3 12l9 5 9-5M3 16l9 5 9-5"/></svg>Challenge</div>
    <div class="tab"><svg width="18" height="18" viewBox="0 0 24 24" fill="#aaa"><circle cx="5" cy="12" r="1.6"/><circle cx="12" cy="12" r="1.6"/><circle cx="19" cy="12" r="1.6"/></svg>Menü</div>
  </nav>
</section>

<div class="label" style="left:40px;top:2360px">13. Settings</div>
<div class="label" style="left:427px;top:2350px">14. Menu / Navigation Drawer</div>

<!-- 13 Settings -->
<section class="phone" style="left:41px;top:2385px;height:702px">
  <h1 class="abs" style="left:33px;top:50px;font-size:25px;font-weight:500">Einstellungen</h1>
  <p class="sect" style="top:105px">Präferenzen</p>
  <div class="group" style="top:128px">
    <div class="row">Mitteilungen<span style="width:36px;height:20px;border-radius:10px;background:var(--lime);position:relative"><i style="position:absolute;right:2px;top:2px;width:16px;height:16px;border-radius:50%;background:#fff"></i></span></div>
    <div class="row">Daily Reminder Zeit<span class="val">08:00</span></div>
  </div>
  <p class="sect" style="top:251px">Account &amp; Daten</p>
  <div class="group" style="top:273px">
    <div class="row">Profil bearbeiten<svg width="10" height="10" viewBox="0 0 10 10" fill="none" stroke="#aaa" stroke-width="1.2"><path d="M3.5 2l3 3-3 3"/></svg></div>
    <div class="row">Exportiere meine Daten<svg width="12" height="12" viewBox="0 0 12 12" fill="none" stroke="#aaa" stroke-width="1.1"><path d="M6 1.5v6M3.5 5L6 7.5 8.5 5M1.5 8.5v2h9v-2"/></svg></div>
    <div class="row">Privatsphäre<svg width="12" height="12" viewBox="0 0 12 12" fill="none" stroke="#aaa" stroke-width="1.1"><rect x="2.5" y="5.5" width="7" height="5" rx="1"/><path d="M4 5.5V4a2 2 0 0 1 4 0v1.5"/></svg></div>
  </div>
  <p class="sect" style="top:444px">Support</p>
  <div class="group" style="top:466px">
    <div class="row">Hilfe &amp; FAQ<svg width="12" height="12" viewBox="0 0 12 12" fill="none" stroke="#aaa" stroke-width="1.1"><path d="M7 1.5h3.5V5M10.5 1.5L6 6M9 7v3.5H1.5V3H5"/></svg></div>
  </div>
  <p class="abs center" style="top:570px;font-size:12px;color:var(--red)">Abmelden</p>
  <p class="abs center" style="top:604px;font-size:8px;color:#bbb">Version 1.0.2 • Build 2490</p>
  <nav class="tabbar" style="top:620px">
    <div class="tab"><svg width="18" height="18" viewBox="0 0 24 24" fill="none" stroke="#aaa" stroke-width="1.8"><path d="M3 10l9-7 9 7v11H3z"/><path d="M10 21v-6h4v6"/></svg>Home</div>
    <div class="tab"><svg width="18" height="18" viewBox="0 0 24 24" fill="none" stroke="#aaa" stroke-width="1.8"><path d="M6 20v-6M12 20V4M18 20v-9"/></svg>Statistik</div>
    <div class="tab"><svg width="18" height="18" viewBox="0 0 24 24" fill="none" stroke="#aaa" stroke-width="1.6"><path d="M12 3l9 5-9 5-9-5z"/><path d="M3 12l9 5 9-5M3 16l9 5 9-5"/></svg>Challenge</div>
    <div class="tab on"><svg width="18" height="18" viewBox="0 0 24 24" fill="#5aa300"><circle cx="5" cy="12" r="1.8"/><circle cx="12" cy="12" r="1.8"/><circle cx="19" cy="12" r="1.8"/></svg>Menü</div>
  </nav>
</section>

<!-- 14 Menu drawer -->
<section class="phone" style="left:427px;top:2377px;height:702px;border:6px solid #fff">
  <div class="abs" style="left:0;right:0;top:0;height:380px;background:linear-gradient(180deg,#cfcfcf,#b9b9b9)">
    <p style="position:absolute;left:24px;top:45px;font-size:11px;color:#8d8d8d">Dienstag, 24. Okt</p>
    <p style="position:absolute;left:24px;top:65px;font-size:20px;font-weight:500;color:#6e6e6e">Guten Morgen, Anna</p>
  </div>
  <div class="abs" style="left:0;right:0;top:354px;bottom:0;background:#fff;border-radius:30px 30px 0 0">
    <i class="abs" style="left:147px;top:20px;width:40px;height:4px;border-radius:2px;background:#ddd"></i>
    <div class="abs" style="left:18px;right:18px;top:52px;display:flex;justify-content:space-between;font-size:10px;color:#777;text-align:center">
      <div><div class="round" style="position:static;width:45px;height:45px;border:1px solid #e6e6e6;margin:0 auto 12px"><svg width="16" height="16" viewBox="0 0 24 24" fill="none" stroke="#222" stroke-width="1.8"><circle cx="12" cy="8" r="4"/><path d="M4 21c1-5 15-5 16 0"/></svg></div>Profil</div>
      <div><div class="round" style="position:static;width:45px;height:45px;border:1px solid #e6e6e6;margin:0 auto 12px"><svg width="16" height="16" viewBox="0 0 24 24" fill="none" stroke="#222" stroke-width="1.8"><circle cx="12" cy="12" r="3"/><path d="M12 2v3M12 19v3M2 12h3M19 12h3M5 5l2 2M17 17l2 2M5 19l2-2M17 7l2-2"/></svg></div>Einstellungen</div>
      <div><div class="round" style="position:static;width:45px;height:45px;border:1px solid #e6e6e6;margin:0 auto 12px"><svg width="16" height="16" viewBox="0 0 24 24" fill="none" stroke="#222" stroke-width="1.8"><path d="M6 16V11a6 6 0 0 1 12 0v5l2 2H4z"/><path d="M10 21h4"/></svg></div>Mitteilungen</div>
      <div><div class="round" style="position:static;width:45px;height:45px;border:1px solid #e6e6e6;margin:0 auto 12px"><svg width="16" height="16" viewBox="0 0 24 24" fill="none" stroke="#222" stroke-width="1.8"><circle cx="12" cy="12" r="9"/><path d="M9.5 9.5a2.5 2.5 0 1 1 3.5 2.3c-.7.3-1 .9-1 1.7M12 17v.2"/></svg></div>Hilfe</div>
    </div>
    <div class="abs" style="left:30px;right:30px;top:160px;font-size:13px;font-weight:500">
      <div style="display:flex;align-items:center;gap:12px;height:53px"><svg width="14" height="14" viewBox="0 0 24 24" fill="none" stroke="#444" stroke-width="1.8"><path d="M12 3l8 3v6c0 5-4 8-8 9-4-1-8-4-8-9V6z"/></svg><span style="flex:1">Datenschutz &amp; AGB</span><svg width="10" height="10" viewBox="0 0 10 10" fill="none" stroke="#aaa" stroke-width="1.2"><path d="M3.5 2l3 3-3 3"/></svg></div>
      <div style="display:flex;align-items:center;gap:12px;height:53px"><svg width="14" height="14" viewBox="0 0 24 24" fill="none" stroke="#444" stroke-width="1.8" stroke-linejoin="round"><path d="M12 3l2.8 5.8 6.2.9-4.5 4.4 1 6.2L12 17.4 6.5 20.3l1-6.2L3 9.7l6.2-.9z"/></svg><span style="flex:1">App Bewerten</span><svg width="10" height="10" viewBox="0 0 10 10" fill="none" stroke="#aaa" stroke-width="1.2"><path d="M3.5 2l3 3-3 3"/></svg></div>
      <div style="display:flex;align-items:center;gap:12px;height:53px;color:var(--red)"><svg width="14" height="14" viewBox="0 0 24 24" fill="none" stroke="#e0352b" stroke-width="1.8"><path d="M10 4H4v16h6M14 8l4 4-4 4M18 12H9"/></svg>Abmelden</div>
    </div>
  </div>
</section>

</body>
</html>
```